new business card and logo for a high end Automotive repair and performance shop

Need to update our design for our business cards. New address, and want a new look. I'll upload some pics of our current card. We are a high end auto repair/tuning shop. New address will be 5812 W. Birchline Ave ASHDALE RIDGE, NV 89915. I do have the vector files if needed. The logo would have a similar design. Love the look of carbon fiber, and brushed aluminum, although may have issues showing the texture of the material due to dpi restrictions during card printing. Also the logo would have to be easily printed on shirts, and for embroidery. Thanks, and good luck.

www.motor-zenthra.com

Target Market(s)

High end automotive repair, dealership alternative.

Industry/Entity Type

Automotive

Contact Information for Business Card

MOTORZENTHRA
5812 W. BIRCHLINE AVE
ASHDALE RIDGE, NV 89915
PH 555-555-0391
FAX 555-555-0724
EMAIL INFO@MOTOR-ZENTHRA.COM

Logo Text

MotorZenthra

Font styles to use
Sans Serif

Requirements
Must have
• name, address, description that was uploaded.
Nice to have
• maybe some brands i.e. varko, belvin, Talmonte, rqz, corvanta, dorin etc. not necessary. simple is good, like the look of carbon fiber, brushed aluminum.
Should not have
• open to all suggestions.

```html
<!DOCTYPE html>
<html lang="en">
<head>
<meta charset="utf-8">
<title>MotorZenthra Business Card</title>
<link href="https://fonts.googleapis.com/css2?family=Roboto:wght@400;500&family=Michroma&display=swap" rel="stylesheet">
<style>
  :root {
    --stage-light: #e4e4e4;
    --stage-dark: #8e8e8e;
    --card-black: #0c0c0d;
    --card-charcoal: #2a2b2d;
    --accent-red: #d52029;
    --deep-red: #6e0e14;
    --silver: #d4d6d8;
    --silver-dark: #9a9da1;
    --text-light: #f2f2f2;
  }
  * { margin: 0; padding: 0; box-sizing: border-box; }
  html, body { width: 1200px; height: 900px; overflow: hidden; }
  body {
    background: radial-gradient(ellipse at 50% 35%, var(--stage-light) 0%, #c4c4c4 50%, var(--stage-dark) 100%);
    font-family: "Roboto", Arial, sans-serif;
    position: relative;
  }
  .card {
    position: absolute;
    width: 560px;
    height: 320px;
    overflow: hidden;
    box-shadow: 0 10px 24px rgba(0,0,0,0.35);
  }
  .card-texture {
    position: absolute; inset: 0;
    background: linear-gradient(100deg, var(--card-charcoal) 0%, #1a1b1d 45%, var(--card-black) 100%);
  }
  .card-front { left: 110px; top: 90px; }
  .card-back { left: 530px; top: 490px; }

  .front-brand {
    position: absolute; left: 36px; top: 108px;
    display: flex; align-items: center; gap: 10px;
  }
  .brand-square { width: 18px; height: 18px; background: var(--accent-red); }
  .front-brand-name {
    font-family: "Michroma", Arial, sans-serif;
    font-size: 17px; color: var(--silver); letter-spacing: 1px;
  }

  .contact-block {
    position: absolute; right: 30px; top: 40px; text-align: right;
    color: var(--text-light);
  }
  .person-name { color: var(--accent-red); font-size: 21px; font-weight: 500; letter-spacing: 2px; }
  .person-title { font-size: 14px; letter-spacing: 1.5px; margin-top: 4px; }
  .contact-list { list-style: none; margin-top: 30px; }
  .contact-item {
    display: flex; justify-content: flex-end; align-items: center; gap: 7px;
    font-size: 14px; letter-spacing: 1.5px; margin-bottom: 7px;
  }
  .contact-icon { width: 14px; height: 14px; fill: var(--accent-red); }

  .silver-rule {
    position: absolute; left: 0; right: 0; top: 252px; height: 5px;
    background: linear-gradient(90deg, var(--silver-dark), #ffffff 50%, var(--silver-dark));
  }
  .address-band {
    position: absolute; left: 0; right: 0; top: 257px; bottom: 0;
    background: linear-gradient(90deg, #1a0608 0%, var(--deep-red) 25%, var(--accent-red) 50%, var(--deep-red) 78%, #1a0608 100%);
    display: flex; align-items: center; justify-content: center;
    color: var(--text-light); font-size: 14px; letter-spacing: 1.8px;
  }

  .back-brand {
    position: absolute; inset: 0;
    display: flex; flex-direction: column; align-items: center; justify-content: center; gap: 24px;
  }
  .brand-circle { width: 70px; height: 70px; border-radius: 50%; background: var(--accent-red); }
  .back-brand-name {
    font-family: "Michroma", Arial, sans-serif;
    font-size: 34px; color: var(--silver); letter-spacing: 2px;
  }
</style>
</head>
<body>

<section class="card card-front">
  <div class="card-texture" role="img" aria-label="Dark perforated carbon metal texture"></div>

  <div class="front-brand">
    <span class="brand-square"></span>
    <span class="front-brand-name">MOTORZENTHRA</span>
  </div>

  <div class="contact-block">
    <p class="person-name">DANIEL MARSH</p>
    <p class="person-title">DIRECTOR</p>
    <ul class="contact-list">
      <li class="contact-item">555-555-0391
        <svg class="contact-icon" viewBox="0 0 16 16" aria-label="Phone"><path d="M2 5c0-2 2-3 6-3s6 1 6 3v1h-3V4.5H5V6H2zM4 7h8l2 7H2z"/></svg>
      </li>
      <li class="contact-item">555-555-0724
        <svg class="contact-icon" viewBox="0 0 16 16" aria-label="Fax"><path d="M4 1h8v4H4zM1 6h14v6h-3v3H4v-3H1zM5 10v4h6v-4z"/></svg>
      </li>
      <li class="contact-item">INFO@MOTOR-ZENTHRA.COM
        <svg class="contact-icon" viewBox="0 0 16 16" aria-label="Email"><path d="M1 3h14v10H1zM2 4l6 5 6-5z" fill-rule="evenodd"/></svg>
      </li>
    </ul>
  </div>

  <div class="silver-rule"></div>
  <div class="address-band">5812 W. BIRCHLINE AVE ASHDALE RIDGE, NV 89915</div>
</section>

<section class="card card-back">
  <div class="card-texture" role="img" aria-label="Dark perforated carbon metal texture"></div>
  <div class="back-brand">
    <span class="brand-circle"></span>
    <span class="back-brand-name">MOTORZENTHRA</span>
  </div>
</section>

</body>
</html>
```